hotel's Website

Hotels website redesign for reference pictures, logo etc see http://restwellmarlow.co.uk/

1. 2-3 Special offers on the main page.
2. Booking calender
3. Location Map
4. Picture gallery.
5. Journeyscope reviews.
6. short description
7. Social Media sharing.
8 Phone number and address.

Industry/Entity Type

Hotel

Requirements
Must have
• 1. 2-3 Special offers on the main page.
2. Booking calender
3. Location Map
4. Picture gallery.
5. Journeyscope reviews.
6. short description
7. Social Media sharing.

```html
<!DOCTYPE html>
<html lang="en">
<head>
<meta charset="utf-8">
<title>Restwell Inn &amp; Suites</title>
<link rel="stylesheet" href="https://fonts.googleapis.com/css2?family=Arimo:wght@400;700&family=Great+Vibes&family=Open+Sans:wght@400&display=swap">
<style>
:root{
  --teal:#0d93b6;
  --teal-dark:#0a7595;
  --teal-fold:#5a6a70;
  --panel:#f4f4f4;
  --line:#e2e2e2;
  --text:#222222;
  --muted:#9a9a9a;
  --grey-btn:#c6c6c6;
  --input:#e9e9e9;
  --input-border:#cfcfcf;
  --white:#ffffff;
  --navy:#1d3f8f;
}
*{box-sizing:border-box;margin:0;padding:0}
html,body{width:842px;height:1200px;overflow:hidden;background:var(--white)}
body{position:relative;font-family:"Arimo",Arial,sans-serif;color:var(--text)}
.abs{position:absolute}

/* hero */
.hero{left:0;top:0;width:842px;height:350px;
  background:linear-gradient(100deg,#b98a5c 0%,#e8d8c4 28%,#f1ece6 45%,#c9272b 62%,#e7d6c0 80%,#c58f55 100%)}
.brand-panel{left:0;top:24px;width:189px;height:132px}
.brand-name{left:22px;top:62px;width:110px;color:var(--navy);font-size:15px;font-weight:700;line-height:1.2}
.pin-tab{left:386px;top:0;width:83px;height:48px;background:var(--white);border-radius:0 0 42px 42px}
.slide-arrow{width:60px;height:60px;border-radius:50%;background:rgba(255,255,255,.35);top:256px}
.slide-arrow svg{display:block;margin:18px auto}

/* nav */
.nav-fold{top:350px;width:0;height:0;border-top:13px solid var(--teal-fold)}
.nav-fold.left{left:77px;border-left:8px solid transparent}
.nav-fold.right{left:757px;border-right:8px solid transparent}
.main-nav{left:77px;top:325px;width:688px;height:38px;background:linear-gradient(var(--teal),var(--teal-dark))}
.main-nav a{position:absolute;top:11px;color:var(--white);text-decoration:none;font-size:14.5px;letter-spacing:.2px}

/* booking */
.booking{left:76px;top:382px;width:688px;height:76px;background:#f7f7f7;border-top:1px solid var(--line);border-bottom:1px solid var(--line)}
.booking-tag{left:76px;top:402px;width:110px;height:32px}
.booking-tag span{position:absolute;left:12px;top:9px;color:var(--white);font-size:13px}
.field{height:26px;background:var(--input);border:1px solid var(--input-border);border-radius:3px;top:405px}
.field-label{top:412px;font-size:11.5px;color:var(--muted)}
.check-btn{left:688px;top:403px;width:61px;height:31px;background:var(--teal);color:var(--white);font-size:13px;text-align:center;line-height:31px;border-radius:2px}

/* welcome */
.rule{height:1px;background:#9a9a9a;top:516px;width:120px}
.welcome-title{left:0;width:842px;top:498px;text-align:center;font-family:"Great Vibes",cursive;font-size:29px;color:#777}
.intro{left:0;width:842px;top:546px;text-align:center;font-family:"Open Sans",Arial,sans-serif;font-size:9.6px;line-height:13.8px;color:var(--muted)}
.grey-btn{top:621px;width:103px;height:28px;background:var(--grey-btn);color:var(--white);font-size:12.5px;text-align:center;line-height:28px;border-radius:2px}
.or{left:410px;top:622px;font-family:"Great Vibes",cursive;font-size:21px;color:#666}

/* features */
.features{left:76px;top:685px;width:688px;height:276px;background:var(--panel);border-top:1px solid var(--line);border-bottom:1px solid var(--line)}
.photo{display:block}
.card-title{text-align:center;font-size:12.5px;color:var(--text);width:191px}
.card-text{text-align:center;font-family:"Open Sans",Arial,sans-serif;font-size:9.6px;line-height:13.8px;color:var(--muted);width:191px}
.read-more{width:74px;height:24px;background:var(--teal);color:var(--white);font-size:11px;text-align:center;line-height:24px;border-radius:2px}

/* footer blocks */
.footer{left:76px;top:994px;width:688px;height:206px;background:var(--panel);border-top:1px solid var(--line)}
.footer-title{top:1018px;font-size:12.5px;letter-spacing:.3px}
.quote{left:100px;width:181px;font-family:"Open Sans",Arial,sans-serif;font-size:9.6px;line-height:13.8px;color:var(--muted);text-align:justify}
.quote b{color:var(--teal);font-weight:400}
.newsletter-text{left:325px;top:1056px;width:181px;font-family:"Open Sans",Arial,sans-serif;font-size:9.6px;line-height:13.8px;color:var(--muted);text-align:justify}
.email-input{left:325px;top:1107px;width:182px;height:26px;background:var(--input);border:1px solid var(--input-border);border-radius:3px;font-family:"Open Sans",Arial,sans-serif;font-size:9px;color:#aaa;text-align:center;line-height:24px}
.subscribe{left:325px;top:1146px;width:105px;height:25px;background:var(--teal);color:var(--white);font-size:11px;text-align:center;line-height:25px;border-radius:2px}
.review-mark{left:552px;top:1078px;width:180px;height:80px}
.review-name{position:absolute;left:0;top:48px;width:180px;text-align:center;font-size:25px;color:var(--text)}
.review-dot{position:absolute;left:68px;top:0;width:44px;height:44px;border-radius:50%;background:var(--text)}
</style>
</head>
<body>

<header>
  <div class="abs hero" role="img" aria-label="Hotel bedroom with white beds, red throws and cushions, a bright window with red curtains"></div>

  <svg class="abs brand-panel" viewBox="0 0 189 132" aria-hidden="true">
    <polygon points="0,0 120,0 189,66 120,132 0,132" fill="rgba(255,255,255,.45)"/>
  </svg>
  <div class="abs brand-name">Restwell<br>Inn &amp; Suites</div>

  <div class="abs pin-tab">
    <svg width="20" height="30" viewBox="0 0 20 30" style="display:block;margin:6px auto 0">
      <path d="M10 0C4.5 0 0 4.4 0 9.8 0 17 10 30 10 30s10-13 10-20.2C20 4.4 15.5 0 10 0z" fill="var(--teal)"/>
      <circle cx="10" cy="9.5" r="3.6" fill="var(--white)"/>
    </svg>
  </div>

  <div class="abs slide-arrow" style="left:75px">
    <svg width="16" height="24" viewBox="0 0 16 24"><polyline points="13,2 3,12 13,22" fill="none" stroke="var(--white)" stroke-width="4"/></svg>
  </div>
  <div class="abs slide-arrow" style="left:705px">
    <svg width="16" height="24" viewBox="0 0 16 24"><polyline points="3,2 13,12 3,22" fill="none" stroke="var(--white)" stroke-width="4"/></svg>
  </div>

  <div class="abs nav-fold left"></div>
  <div class="abs nav-fold right"></div>
  <nav class="abs main-nav">
    <a href="#" style="left:65px">HOME</a>
    <a href="#" style="left:148px">ABOUT US</a>
    <a href="#" style="left:258px">ROOMS</a>
    <a href="#" style="left:341px">PAGES</a>
    <a href="#" style="left:423px">EVENTS</a>
    <a href="#" style="left:533px">CONTACT US</a>
  </nav>
</header>

<section aria-label="Booking">
  <div class="abs booking"></div>
  <div class="abs booking-tag">
    <svg width="110" height="32" viewBox="0 0 110 32" style="position:absolute;left:0;top:0"><polygon points="0,0 85,0 110,16 85,32 0,32" fill="var(--teal)"/></svg>
    <span>BOOKING</span>
  </div>
  <div class="abs field" style="left:193px;width:128px">
    <svg width="16" height="16" viewBox="0 0 16 16" style="position:absolute;right:6px;top:4px">
      <rect x="1" y="2" width="14" height="13" fill="none" stroke="#cfcfcf" stroke-width="1.2"/>
      <line x1="1" y1="5.5" x2="15" y2="5.5" stroke="#cfcfcf" stroke-width="1.5"/>
      <path d="M4.5 8h2M8 8h2M11.5 8h2M4.5 11h2M8 11h2M11.5 11h2" stroke="#cfcfcf" stroke-width="1.5"/>
    </svg>
  </div>
  <div class="abs field-label" style="left:334px">Nights</div>
  <div class="abs field" style="left:391px;width:45px"></div>
  <div class="abs field-label" style="left:454px">Adults</div>
  <div class="abs field" style="left:502px;width:44px"></div>
  <div class="abs field-label" style="left:563px">Childrens</div>
  <div class="abs field" style="left:624px;width:45px"></div>
  <div class="abs check-btn">CHECK</div>
</section>

<section aria-label="Welcome">
  <div class="abs rule" style="left:77px"></div>
  <div class="abs rule" style="left:643px"></div>
  <h1 class="abs welcome-title" style="font-weight:400">Welcome to Restwell Inn &amp; Suites</h1>
  <p class="abs intro">Lorem ipsum dolor sit amet, consectetur adipiscing elit.<br>Aliquam suscipit erat non tellus vehicula, et euismod felis convallis. Morbi sed massa eget<br>eros sodales aliquet sit amet sit amet felis. Vestibulum sit amet vehicula turpis.<br>Duis luctus ipsum quis dui ornare ultrices.</p>
  <div class="abs grey-btn" style="left:288px">Take a Tour</div>
  <div class="abs or">or</div>
  <div class="abs grey-btn" style="left:455px">Book Now</div>
</section>

<section aria-label="Special offers">
  <div class="abs features"></div>
  <svg class="abs" style="left:289px;top:708px" width="261" height="140" viewBox="0 0 261 140" aria-hidden="true">
    <polygon points="0,0 35,0 35,140" fill="#dedede"/>
    <polygon points="226,0 261,0 226,140" fill="#dedede"/>
  </svg>

  <div class="abs photo" style="left:98px;top:709px;width:191px;height:104px;background:linear-gradient(#2a2440,#7a4a6a 55%,#c99a4a 80%,#2c2a30)" role="img" aria-label="City skyline at night with an illuminated observation wheel by the river"></div>
  <h2 class="abs card-title" style="left:98px;top:825px;font-weight:400">EXPLORE LONDON</h2>
  <p class="abs card-text" style="left:98px;top:848px">Lorem ipsum dolor sit amet,<br>consectetur adipiscing elit. Aliquam<br>suscipit erat non tellus vehicula,<br>et euismod felis convallis.</p>
  <div class="abs read-more" style="left:157px;top:917px">Read More</div>

  <div class="abs photo" style="left:324px;top:708px;width:191px;height:140px;background:linear-gradient(100deg,#d9c9b4 0%,#8f2a2a 25%,#e3dcd2 45%,#d42e35 65%,#c9262c 100%)" role="img" aria-label="Twin hotel room with red wall, white beds and red curtains"></div>
  <h2 class="abs card-title" style="left:324px;top:859px;font-weight:400">SPECIAL OFFERS</h2>
  <p class="abs card-text" style="left:324px;top:883px">Lorem ipsum dolor sit amet,<br>consectetur adipiscing elit. Aliquam<br>suscipit erat non tellus vehicula.</p>
  <div class="abs read-more" style="left:382px;top:929px">Read More</div>

  <div class="abs photo" style="left:550px;top:708px;width:191px;height:104px;background:linear-gradient(110deg,#e9a04a 0%,#f4efe8 35%,#d99a4e 60%,#c9323a 80%,#f0c040 100%)" role="img" aria-label="Breakfast table with croissants, coffee and orange juice"></div>
  <h2 class="abs card-title" style="left:550px;top:826px;font-weight:400">STAY IN COMFORT</h2>
  <p class="abs card-text" style="left:550px;top:849px">Lorem ipsum dolor sit amet,<br>consectetur adipiscing elit. Aliquam<br>suscipit erat non tellus vehicula,<br>et euismod felis convallis.</p>
  <div class="abs read-more" style="left:608px;top:916px">Read More</div>
</section>

<footer>
  <div class="abs footer"></div>

  <h3 class="abs footer-title" style="left:98px;font-weight:400">CUSTOMER REVIEWS</h3>
  <p class="abs quote" style="top:1056px"><b>"</b>Lorem ipsum dolor sit amet, consectetur adipiscing elit, seddo eiusmod tempor.<b>"</b></p>
  <p class="abs quote" style="top:1134px"><b>"</b>Lorem ipsum dolor sit amet, consectetur adipiscing elit, seddo eiusmod tempor.<b>"</b></p>

  <h3 class="abs footer-title" style="left:325px;font-weight:400">STAY IN TOUCH</h3>
  <p class="abs newsletter-text">Sign up for our newsletter for latest news from Restwell Inn and Suites - King's Cross</p>
  <div class="abs email-input">----- Enter Email Address -----</div>
  <div class="abs subscribe">Subscribe</div>

  <h3 class="abs footer-title" style="left:551px;font-weight:400">JOURNEYSCOPE</h3>
  <div class="abs review-mark">
    <div class="review-dot"></div>
    <div class="review-name">journeyscope</div>
  </div>
</footer>

</body>
</html>
```